business cards for a real estate investment company
Corva Homebuyers
Hi,
Can you check the draft #130, #131, #132, #133, #134, #135 and #136.
Thanks
Hello vostrapixel. I was really hoping to see some updated designs. I like what you've done so far and was hoping to give you the money. The drafts i mentioned above are almost perfect except< again, I'd love to see the term "Homebuilders" along with the logo so it's more obvious what services we provide. Thank you and I hope to see some more great work
TK/RPF/NW Team
Hello. One more note! I really like #45 as well. Same notes and changes apply. Thanks again
Hi vostrapixel. I really love design number 63. One thing I would like you to incorporate is "Homebuyers LLC". Maybe place the phrase somewhere around the corva logo. I'll trust your sensibility. Looking back, I really like number 47 as well, but with 63's backside, and again including "Homebuyers LLC". Thank you so much and I look forward to your modifications.

```html
<!DOCTYPE html>
<html lang="en">
<head>
<meta charset="utf-8">
<title>Corva Homebuyers – Business Card</title>
<link href="https://fonts.googleapis.com/css2?family=Michroma&family=Montserrat:wght@800&display=swap" rel="stylesheet">
<style>
  :root {
    --page-bg: #e9e6e1;
    --card-white: #ffffff;
    --brand-blue: #1f64c4;
    --brand-blue-deep: #124a9e;
    --brand-blue-light: #2f7ad8;
    --brand-green: #5aa72c;
    --brand-green-light: #8cc63f;
    --text-light: #ffffff;
    --divider: rgba(255,255,255,0.7);
  }
  html, body {
    margin: 0;
    padding: 0;
    width: 1200px;
    height: 914px;
    overflow: hidden;
    background: var(--page-bg);
  }
  .business-card {
    position: absolute;
    left: 100px;
    top: 171px;
    width: 1000px;
    height: 572px;
    background: var(--card-white);
    box-shadow: 0 10px 30px rgba(0,0,0,0.18);
    overflow: hidden;
  }
  .card-waves {
    position: absolute;
    inset: 0;
  }
  .brand {
    position: absolute;
    top: 70px;
    left: 0;
    width: 100%;
    text-align: center;
  }
  .brand-mark {
    margin: 0;
    font-family: "Montserrat", sans-serif;
    font-weight: 800;
    font-size: 88px;
    line-height: 1;
    color: var(--brand-blue);
    letter-spacing: 1px;
  }
  .brand-tagline {
    margin: 8px 0 0;
    font-family: "Michroma", sans-serif;
    font-size: 15px;
    letter-spacing: 4px;
    text-transform: uppercase;
    color: var(--brand-green);
  }
  .holder {
    position: absolute;
    top: 338px;
    right: 536px;
    text-align right;
    text-align: right;
    font-family: "Michroma", sans-serif;
    color: var(--text-light);
    text-transform: uppercase;
    letter-spacing: 2px;
  }
  .holder-name { font-size: 20px; margin: 0 0 8px; font-weight: 400; }
  .holder-title { font-size: 16px; margin: 0; }
  .divider {
    position: absolute;
    left: 484px;
    top: 330px;
    width: 2px;
    height: 110px;
    background: var(--divider);
  }
  .contact-list {
    position: absolute;
    left: 502px;
    top: 330px;
    margin: 0;
    padding: 0;
    list-style: none;
    font-family: "Michroma", sans-serif;
    font-size: 13px;
    color: var(--text-light);
    text-transform: uppercase;
    letter-spacing: 1px;
    white-space: nowrap;
  }
  .contact-item {
    display: flex;
    align-items: center;
    gap: 10px;
    height: 36px;
  }
  .contact-icon { width: 18px; height: 18px; flex: none; }
</style>
</head>
<body>
<div class="business-card">
  <svg class="card-waves" viewBox="0 0 1000 572" preserveAspectRatio="none">
    <defs>
      <linearGradient id="blueBand" x1="0" y1="0" x2="0" y2="1">
        <stop offset="0" stop-color="#2f7ad8"/>
        <stop offset="1" stop-color="#124a9e"/>
      </linearGradient>
      <linearGradient id="greenBand" x1="0" y1="0" x2="1" y2="0">
        <stop offset="0" stop-color="#8cc63f"/>
        <stop offset="1" stop-color="#5aa72c"/>
      </linearGradient>
    </defs>
    <path d="M0 205 C 240 300, 520 300, 1000 195 L1000 245 C 560 330, 260 330, 0 240 Z" fill="url(#greenBand)"/>
    <path d="M0 238 C 250 335, 560 335, 1000 240 L1000 572 L0 572 Z" fill="url(#blueBand)"/>
    <path d="M0 258 C 260 350, 560 350, 1000 258" fill="none" stroke="rgba(255,255,255,0.35)" stroke-width="2"/>
  </svg>

  <div class="brand">
    <p class="brand-mark">Corva</p>
    <p class="brand-tagline">Homebuyers LLC</p>
  </div>

  <div class="holder">
    <p class="holder-name">Dan Torquell</p>
    <p class="holder-title">Managing Partner</p>
  </div>

  <div class="divider"></div>

  <ul class="contact-list">
    <li class="contact-item">
      <svg class="contact-icon" viewBox="0 0 18 18"><circle cx="9" cy="9" r="9" fill="#fff"/><path d="M6 4.5l1.6 0 .8 2.3-1 .8a6 6 0 0 0 3 3l.8-1 2.3.8 0 1.6c0 .6-.5 1-1 1A8 8 0 0 1 5 5.5c0-.5.4-1 1-1z" fill="#1f64c4"/></svg>
      <span>555-014-0187</span>
    </li>
    <li class="contact-item">
      <svg class="contact-icon" viewBox="0 0 18 18"><circle cx="9" cy="9" r="9" fill="#fff"/><rect x="4.5" y="6" width="9" height="6.5" fill="none" stroke="#1f64c4" stroke-width="1.3"/><path d="M4.5 6l4.5 3.5L13.5 6" fill="none" stroke="#1f64c4" stroke-width="1.3"/></svg>
      <span>corvahomebuyers@corvamail.com</span>
    </li>
    <li class="contact-item">
      <svg class="contact-icon" viewBox="0 0 18 18"><circle cx="9" cy="9" r="9" fill="#fff"/><circle cx="9" cy="9" r="4.8" fill="none" stroke="#1f64c4" stroke-width="1.2"/><path d="M4.2 9h9.6M9 4.2c-2 2.6-2 7 0 9.6M9 4.2c2 2.6 2 7 0 9.6" fill="none" stroke="#1f64c4" stroke-width="1"/></svg>
      <span>www.corvahomebuyers.com</span>
    </li>
  </ul>
</div>
</body>
</html>
```